Business Advisory Cards in canvas model

I need a business card to start as an individual advising in business since I am "Bachelor in Business Creation and business innovation" I would like the "Canvas Model" (basic tool to land a business) to represent a part of the logo because it is the simplest and useful model to start, I will advise on business innovation and business creation. Detail: it can be formal, dynamic, colorful, that draws attention, adapted to the millenians.

Target Market(s)

People who want to create their own company. People seeking advice on: negotiation, innovation in business, desing thingking, business creation, coaching in organizational operations, business plan and canvas model.

Contact Information for Business Card

Puede ser colorida pero formal para negociar, que se vea moderna adaptada a los millenians, que se enfoque en “el modelo canvas”.
Que ocupe toda la tarjeta de ambos lados todo el diseño.

Font styles to use
Sans Serif

Colors

Designer to choose colors to be used in the design.

Requirements
Must have
• Canvas model
Nice to have
• Make it a card that makes the person who receives it want to contact the owner of the card. Make it pleasing to the eye.
Should not have
• Negative images, colors that are lost or damage the eyesight.

```html
<!DOCTYPE html>
<html lang="es">
<head>
<meta charset="utf-8">
<title>Daniel Ocampo – Tarjeta de presentación</title>
<link href="https://fonts.googleapis.com/css2?family=Fira+Sans:wght@500;600;700&display=swap" rel="stylesheet">
<style>
  :root {
    --page: #ffffff;
    --blue: #1076bd;
    --blue-dark: #0f5fa0;
    --blue-light: #00aeef;
    --blue-stripe: #27a8e0;
    --green: #36994a;
    --green-icon: #2f9a49;
    --ink: #0f4c81;
    --panel-white: #ffffff;
    --panel-grey: #eceeef;
  }
  html, body {
    margin: 0;
    width: 1200px;
    height: 1200px;
    overflow: hidden;
    background: var(--page);
  }
  .stage { display: block; width: 1200px; height: 1200px; }
  .card-base { fill: var(--blue); }
  .frame { fill: var(--blue-light); }
  .panel-dark { fill: var(--blue-dark); }
  .panel-green { fill: var(--green); }
  .panel-blue { fill: var(--blue); }
  .stripe { fill: var(--blue-stripe); }
  .side { fill: var(--blue); }
  .owner-name {
    font-family: "Fira Sans", sans-serif;
    font-weight: 700;
    font-size: 28px;
    letter-spacing: 2.5px;
    fill: var(--ink);
  }
  .contact-line {
    font-family: "Fira Sans", sans-serif;
    font-weight: 600;
    font-size: 14px;
    letter-spacing: 1.2px;
    fill: var(--ink);
  }
  .icon-bg-green { fill: var(--green-icon); }
  .icon-bg-blue { fill: var(--blue); }
  .icon-glyph { fill: none; stroke: #fff; stroke-width: 2; stroke-linecap: round; stroke-linejoin: round; }
</style>
</head>
<body>
<svg class="stage" viewBox="0 0 1500 1500" xmlns="http://www.w3.org/2000/svg">
  <defs>
    <clipPath id="front-clip"><rect x="404" y="248" width="702" height="394" rx="22"/></clipPath>
    <clipPath id="back-clip"><rect x="404" y="832" width="702" height="395" rx="22"/></clipPath>
    <linearGradient id="back-panel" x1="0" y1="0" x2="0" y2="1">
      <stop offset="0" stop-color="var(--panel-white)"/>
      <stop offset="1" stop-color="var(--panel-grey)"/>
    </linearGradient>
  </defs>

  <!-- Front: canvas model board -->
  <g class="card-front">
    <g clip-path="url(#front-clip)">
      <rect class="card-base" x="404" y="248" width="702" height="394"/>
    </g>
    <polygon class="frame" points="545,248 765,240 965,248 965,478 1088,600 1088,642 780,652 424,642 424,600 545,478"/>

    <g class="canvas-block" role="img" aria-label="Sketched checklist of key activities">
      <polygon class="panel-dark" points="563,265 748,265 748,350 563,382"/>
    </g>
    <g class="canvas-block" role="img" aria-label="Sketched group of people for customer segments">
      <polygon class="panel-green" points="768,265 950,265 950,380 768,350"/>
    </g>
    <g class="canvas-block" role="img" aria-label="Sketched gears and timer for key resources">
      <polygon class="panel-green" points="563,400 738,368 660,525 578,484"/>
    </g>
    <g class="canvas-block" role="img" aria-label="Sketched light bulb for the value proposition">
      <polygon class="panel-blue" points="755,372 840,545 778,590 672,545"/>
    </g>
    <g class="canvas-block" role="img" aria-label="Sketched devices and messages for channels">
      <polygon class="panel-dark" points="775,365 950,400 950,478 860,540"/>
    </g>
    <g class="canvas-block" role="img" aria-label="Sketched bar chart for cost structure">
      <polygon class="panel-dark" points="558,498 665,548 768,606 768,632 440,625 440,610"/>
    </g>
    <g class="canvas-block" role="img" aria-label="Sketched dollar sign for revenue streams">
      <polygon class="panel-green" points="868,548 948,495 1072,605 1072,625 788,632 788,605"/>
    </g>
    <rect x="418" y="380" width="125" height="95" fill="var(--blue)" role="img" aria-label="Sketched partners group for key partnerships"/>
    <rect x="978" y="365" width="112" height="115" fill="var(--blue)" role="img" aria-label="Sketched pie chart for customer relationships"/>
  </g>

  <!-- Back: contact details -->
  <g class="card-back">
    <g clip-path="url(#back-clip)">
      <rect x="404" y="832" width="702" height="395" fill="url(#back-panel)"/>
      <polygon class="stripe" points="404,832 442,832 442,888 563,1000 563,1227 404,1227"/>
      <polygon class="side" points="404,832 424,832 424,888 545,1008 545,1227 404,1227"/>
      <polygon class="stripe" points="1106,832 1070,832 1070,882 948,1000 948,1227 1106,1227"/>
      <polygon class="side" points="1106,832 1088,832 1088,882 965,1008 965,1227 1106,1227"/>
    </g>

    <text class="owner-name" x="630" y="933">DANIEL OCAMPO</text>

    <g class="contact-item">
      <circle class="icon-bg-green" cx="642" cy="982" r="20"/>
      <path class="icon-glyph" d="M632 983 L642 973 L652 983 M635 980 V991 H649 V980 M639 991 V985 H645 V991"/>
      <text class="contact-line" x="672" y="979">45 CALLE FICTICIA, CIUDAD EJEMPLO,</text>
      <text class="contact-line" x="672" y="997">MEXICO</text>
    </g>
    <g class="contact-item">
      <circle class="icon-bg-blue" cx="642" cy="1036" r="20"/>
      <rect class="icon-glyph" x="631" y="1029" width="22" height="15" rx="1.5"/>
      <path class="icon-glyph" d="M631 1030 L642 1039 L653 1030"/>
      <text class="contact-line" x="672" y="1040">HOLA@EJEMPLO.MX</text>
    </g>
    <g class="contact-item">
      <circle class="icon-bg-green" cx="642" cy="1090" r="20"/>
      <path class="icon-glyph" d="M634 1080 C632 1082 632 1086 635 1090 C638 1095 643 1099 647 1100 C650 1101 652 1099 653 1097 L649 1093 L646 1095 C643 1093 640 1090 638 1087 L640 1084 Z"/>
      <text class="contact-line" x="672" y="1096">+52 5550 123 4567</text>
    </g>
    <g class="contact-item">
      <circle class="icon-bg-blue" cx="642" cy="1145" r="20"/>
      <circle class="icon-glyph" cx="642" cy="1145" r="11"/>
      <ellipse class="icon-glyph" cx="642" cy="1145" rx="5" ry="11"/>
      <path class="icon-glyph" d="M631 1145 H653 M633 1139 H651 M633 1151 H651"/>
      <text class="contact-line" x="672" y="1153">WWW.ASESORIANUEVA.MX</text>
    </g>
  </g>
</svg>
</body>
</html>
```